GUARANTEED! Simple website for independent event planner and consultant...

I need a website that is no more than 5 or 6 pages to illustrate who I am and what I can offer to groups who book hotels for meetings and conferences. I have 20 years of experience planning meetings within hotels and I am now ready to go out on my own and help clients choose venues, negotiate contracts and plan effective meetings. I will focus on clients planning meetings in the mountains of Colorado but I am willing to travel as well. I want to work with a person who is collaborative and can direct me on what they need to move the project along quickly. I already have my logo, a hosting site and work e-mail address. Also, I recently hired a photographer to do head shots. Lastly, it important for me to be able to talk on the phone or skype with this person, as needed and I must be able to make changes to my site down the road when necessary...

Target Market(s)

Corporate Groups

Industry/Entity Type

Event Planning

Coding

Coded - Design and coding required

Number of Pages Required

5+ page

Font styles to use
Sans Serif

Requirements
Must have
• About me page, event planning services offered page, task force and consulting work page, testimonials page, page for blogs, page to contact me/request a proposal. May need advice on what else I need...
Nice to have
• I want it to look sharp and professional. I want people to look at my site and know immediately that they can trust me and the work I can do.
• I don't want it to look like it is over the top as I am not a HUGE company but I do want it to be professional and easy to view and navigate.
Should not have
• Bright colors
• My logo is bright orange and black. I have also used dark grey and orange. See below:
• Orange:
• C = 0
• M = 64
• Y = 100
• K = 0
• Gray:
• C = 67
• M = 60
• Y = 59
• K = 45
• Font: Gotham Book and Gotham Bold

```html
<!DOCTYPE html>
<html lang="en">
<head>
<meta charset="utf-8">
<title>Harlow — Colorado Event Management</title>
<link rel="stylesheet" href="https://fonts.googleapis.com/css2?family=Montserrat:wght@300;400;500;600;700&display=swap">
<style>
  :root {
    --orange: #f5821f;
    --charcoal: #1d1d1f;
    --ink: #2b2b2d;
    --grey-text: #6d6d70;
    --light-bg: #f3f3f3;
    --white: #ffffff;
    --black: #000000;
    --line: #d9d9d9;
  }
  * { box-sizing: border-box; margin: 0; padding: 0; }
  html, body { width: 1200px; height: 3500px; overflow: hidden; }
  body {
    font-family: "Montserrat", Arial, sans-serif;
    color: var(--ink);
    background: var(--white);
    position: relative;
  }

  /* Hero */
  .hero {
    position: relative; height: 645px;
    background: linear-gradient(180deg, #3a3a3c 0%, #5b5a58 35%, #4a4744 60%, #2c2a28 100%);
  }
  .hero-photo { position: absolute; inset: 0; }
  .menu-toggle { position: absolute; top: 38px; right: 46px; width: 22px; }
  .menu-toggle span { display: block; height: 2px; background: var(--white); margin-bottom: 5px; }
  .hero-panel {
    position: absolute; left: 420px; top: 190px; width: 360px; height: 180px;
    background: rgba(20,20,22,0.72); text-align: center; padding-top: 40px;
  }
  .brand-title {
    color: var(--white); font-weight: 300; font-size: 40px; letter-spacing: 14px; padding-left: 14px;
  }
  .brand-sub {
    color: #d6d6d6; font-size: 10px; letter-spacing: 3px; text-transform: uppercase; margin-top: 8px;
  }
  .btn {
    display: inline-block; background: var(--orange); color: var(--white);
    font-size: 10px; font-weight: 600; letter-spacing: 2px; text-transform: uppercase;
    padding: 10px 26px; margin-top: 22px;
  }

  /* About */
  .about { position: relative; height: 555px; }
  .about-portrait {
    position: absolute; left: 150px; top: 10px; width: 296px; height: 440px;
    background: linear-gradient(180deg, #b9b4ab 0%, #8f8a83 55%, #5b5752 100%);
  }
  .about-copy { position: absolute; left: 690px; top: 165px; width: 380px; }
  .about-heading {
    font-size: 13px; font-weight: 500; letter-spacing: 3px; text-transform: uppercase;
    line-height: 1.6; color: var(--ink);
  }
  .about-text { font-size: 11px; line-height: 1.75; color: var(--grey-text); margin-top: 18px; }

  /* Services */
  .services { position: relative; height: 545px; background: var(--light-bg); }
  .section-title {
    position: absolute; top: 78px; left: 0; right: 0; text-align: center;
    font-size: 20px; font-weight: 400; letter-spacing: 6px; color: var(--ink);
  }
  .section-title::before, .section-title::after {
    content: ""; display: inline-block; width: 70px; height: 1px; background: var(--line);
    vertical-align: middle; margin: 0 20px;
  }
  .service-grid {
    position: absolute; left: 165px; top: 160px; width: 870px;
    display: grid; grid-template-columns: repeat(3, 265px); column-gap: 37px; row-gap: 28px;
  }
  .service-card { background: var(--white); height: 150px; padding: 22px 24px; }
  .service-icon { width: 22px; height: 22px; stroke: var(--ink); fill: none; stroke-width: 1.5; }
  .service-name {
    font-size: 10px; font-weight: 600; letter-spacing: 1.5px; text-transform: uppercase; margin-top: 10px;
  }
  .service-text { font-size: 9.5px; line-height: 1.6; color: var(--grey-text); margin-top: 8px; }

  /* Spaces */
  .spaces { display: grid; grid-template-columns: 600px 600px; grid-template-rows: 355px 350px; }
  .space-tile { position: relative; display: flex; align-items: center; justify-content: center; }
  .space-office { background: linear-gradient(135deg, #5a3a26 0%, #8d5d3a 50%, #3a2a22 100%); }
  .space-open { background: linear-gradient(135deg, #3b3530 0%, #7a6553 50%, #2e2a27 100%); }
  .space-meeting { background: linear-gradient(135deg, #d7d3cc 0%, #a39c92 50%, #6b645c 100%); }
  .space-community { background: linear-gradient(180deg, #2d3f78 0%, #4b5c9a 45%, #1c2447 100%); }
  .space-label {
    color: var(--white); font-size: 22px; font-weight: 300; letter-spacing: 5px; text-transform: uppercase;
    text-shadow: 0 1px 4px rgba(0,0,0,0.4);
  }

  /* Intro */
  .intro { height: 295px; display: flex; align-items: center; justify-content: center; }
  .intro-text {
    width: 470px; text-align: center; font-size: 10px; letter-spacing: 1.5px; line-height: 1.9;
    text-transform: uppercase; color: var(--grey-text);
  }

  /* Location */
  .location { display: grid; grid-template-columns: 600px 600px; height: 400px; }
  .map-area { position: relative; background: linear-gradient(135deg, #f1f1ef 0%, #e4e4e2 100%); }
  .map-zoom { position: absolute; right: 12px; bottom: 20px; width: 22px; background: var(--white); border: 1px solid var(--line); }
  .map-zoom span { display: block; height: 22px; text-align: center; font-size: 14px; line-height: 22px; color: var(--grey-text); }
  .contact-panel {
    background: linear-gradient(180deg, #2a2a2c 0%, #1c1c1e 100%);
    display: flex; flex-direction: column; align-items: center; justify-content: center;
  }
  .contact-panel .btn { margin-top: 20px; }

  /* Footer */
  .site-footer {
    height: 360px; background: var(--black); text-align: center; padding-top: 110px; color: #9a9a9a;
  }
  .footer-brand { display: inline-flex; align-items: center; gap: 8px; color: var(--orange); font-weight: 700; font-size: 22px; letter-spacing: 3px; }
  .footer-brand i { display: inline-block; width: 10px; height: 10px; background: var(--orange); }
  .footer-tag { font-size: 9px; letter-spacing: 3px; text-transform: uppercase; margin-top: 26px; }
  .footer-phone { font-size: 10px; letter-spacing: 1.5px; color: var(--orange); margin-top: 10px; }
  .social { display: flex; justify-content: center; gap: 22px; margin-top: 24px; }
  .social span { width: 9px; height: 9px; border-radius: 50%; background: #cfcfcf; }
</style>
</head>
<body>

<header class="hero">
  <div class="hero-photo" role="img" aria-label="Photo of an empty boardroom with a long table and leather chairs under a window wall"></div>
  <div class="menu-toggle"><span></span><span></span><span></span></div>
  <div class="hero-panel">
    <h1 class="brand-title">HARLOW</h1>
    <p class="brand-sub">Colorado meetings &amp; events, thoughtfully managed</p>
    <a class="btn">Contact Now</a>
  </div>
</header>

<section class="about">
  <div class="about-portrait" role="img" aria-label="Portrait photo of the event planner standing outdoors in a dark blazer"></div>
  <div class="about-copy">
    <h2 class="about-heading">Harlow is a Colorado based event management company</h2>
    <p class="about-text">Twenty years of planning meetings inside hotels taught us what makes a gathering work. We help corporate groups choose the right venue, negotiate fair contracts and plan sessions that run smoothly, from the Colorado mountains to destinations across the country.</p>
  </div>
</section>

<section class="services">
  <h2 class="section-title">SERVICES</h2>
  <div class="service-grid">
    <article class="service-card">
      <svg class="service-icon" viewBox="0 0 24 24"><rect x="3" y="4" width="18" height="12" rx="1"/><path d="M8 20h8M12 16v4"/></svg>
      <h3 class="service-name">Your Own Desk</h3>
      <p class="service-text">Venue searches, contract review and on-site support shaped around your group, your budget and the goals of every session.</p>
    </article>
    <article class="service-card">
      <svg class="service-icon" viewBox="0 0 24 24"><path d="M4 9h13v5a5 5 0 0 1-5 5H9a5 5 0 0 1-5-5z"/><path d="M17 10h2a2 2 0 0 1 0 4h-2M8 3v3M12 3v3"/></svg>
      <h3 class="service-name">Coffee and Snacks</h3>
      <p class="service-text">Venue searches, contract review and on-site support shaped around your group, your budget and the goals of every session.</p>
    </article>
    <article class="service-card">
      <svg class="service-icon" viewBox="0 0 24 24"><circle cx="12" cy="6" r="2.5"/><circle cx="5" cy="15" r="2.5"/><circle cx="19" cy="15" r="2.5"/><path d="M9 21h6M12 9v12"/></svg>
      <h3 class="service-name">Meeting Rooms</h3>
      <p class="service-text">Venue searches, contract review and on-site support shaped around your group, your budget and the goals of every session.</p>
    </article>
    <article class="service-card">
      <svg class="service-icon" viewBox="0 0 24 24"><rect x="3" y="5" width="18" height="16" rx="1"/><path d="M3 10h18M8 3v4M16 3v4"/></svg>
      <h3 class="service-name">Flexible Dates</h3>
      <p class="service-text">Venue searches, contract review and on-site support shaped around your group, your budget and the goals of every session.</p>
    </article>
    <article class="service-card">
      <svg class="service-icon" viewBox="0 0 24 24"><circle cx="8" cy="8" r="3"/><circle cx="16" cy="8" r="3"/><path d="M2 20c0-4 3-6 6-6s6 2 6 6M12 20c0-4 2-6 4-6s6 2 6 6"/></svg>
      <h3 class="service-name">Community Events</h3>
      <p class="service-text">Venue searches, contract review and on-site support shaped around your group, your budget and the goals of every session.</p>
    </article>
    <article class="service-card">
      <svg class="service-icon" viewBox="0 0 24 24"><path d="M2 9a15 15 0 0 1 20 0M5 13a10 10 0 0 1 14 0M8.5 16.5a5 5 0 0 1 7 0"/><circle cx="12" cy="20" r="1"/></svg>
      <h3 class="service-name">Supply and Internet</h3>
      <p class="service-text">Venue searches, contract review and on-site support shaped around your group, your budget and the goals of every session.</p>
    </article>
  </div>
</section>

<section class="spaces">
  <div class="space-tile space-office" role="img" aria-label="Photo of a private office with a wooden desk and windows"><span class="space-label">Private Office</span></div>
  <div class="space-tile space-open" role="img" aria-label="Photo of an open lounge space with tables under a glass roof"><span class="space-label">Open Space</span></div>
  <div class="space-tile space-meeting" role="img" aria-label="Photo of a bright meeting room with sofas and tall windows"><span class="space-label">Meeting Rooms</span></div>
  <div class="space-tile space-community" role="img" aria-label="Photo of a snowy mountain resort village lit up at dusk"><span class="space-label">Community Events</span></div>
</section>

<section class="intro">
  <p class="intro-text">Your event could look and feel right at home in a venue with stunning meeting rooms, welcoming hosts, dedicated services and careful design. Let us plan your next meeting.</p>
</section>

<section class="location">
  <div class="map-area" role="img" aria-label="Street map of the mountain town showing the office location">
    <div class="map-zoom"><span>+</span><span>−</span></div>
  </div>
  <div class="contact-panel">
    <h2 class="brand-title">HARLOW</h2>
    <p class="brand-sub">Colorado event management</p>
    <a class="btn">Get in Touch</a>
  </div>
</section>

<footer class="site-footer">
  <div class="footer-brand"><i></i>HARLOW</div>
  <p class="footer-tag">Event Consulting</p>
  <p class="footer-phone">Phone: 303 555 0147</p>
  <div class="social"><span></span><span></span><span></span><span></span></div>
</footer>

</body>
</html>
```